Business Card for New Business

Please design a business card using our logo and font files. This is only one card for one person, as listed in details section.

Contact Information for Business Card

Dale Vornhuser

Phone 240.815.3926
Cell 703.461.8075
Email dale@morlenbay.com

www.morlenbay.com

Address
31800 Pinecrest Lane #412
Damascus, MD 20879

Font styles to use
Sans Serif

Requirements
Must have
• Information listed in detail section. Must be standard card size.

```html
<!DOCTYPE html>
<html lang="en">
<head>
<meta charset="utf-8">
<title>Morlenbay Productions – Business Card</title>
<link rel="stylesheet" href="https://fonts.googleapis.com/css2?family=Questrial&family=Khand:wght@600&display=swap">
<style>
  :root {
    --page: #e4e4e4;
    --ink: #0b0b0c;
    --paper: #f4f4f4;
    --rust: #c2461c;
    --rust-dark: #a3411a;
    --text: #2a2a2a;
    --rule: #cfcfcf;
    --web: #e8e8e8;
  }
  * { margin: 0; padding: 0; box-sizing: border-box; }
  html, body { width: 1200px; height: 576px; overflow: hidden; background: var(--page); }
  .canvas { position: relative; width: 1200px; height: 576px; }

  .card {
    position: absolute; top: 139px; width: 484px; height: 292px;
    border-radius: 8px; overflow: hidden;
  }
  .card--back { left: 82px; background: var(--ink); }
  .card--front { left: 600px; background: var(--paper); }

  .wordmark { position: absolute; display: flex; align-items: center; gap: 8px;
    font-family: "Questrial", sans-serif; color: var(--rust); }
  .wordmark__dot { width: 26px; height: 26px; border-radius: 50%; background: var(--rust); flex: none; }
  .wordmark__name { font-size: 40px; line-height: 1; letter-spacing: 0.5px; }

  .card--back .wordmark { left: 0; right: 0; top: 124px; justify-content: center; }

  .card--front .wordmark { left: 30px; top: 116px; }
  .card--front .wordmark__name { font-size: 34px; }
  .card--front .wordmark__dot { width: 22px; height: 22px; }

  .front__divider { position: absolute; left: 254px; top: 65px; width: 1px; height: 136px; background: var(--rule); }

  .details { position: absolute; left: 274px; top: 70px; font-family: "Questrial", sans-serif; color: var(--text); }
  .details__name { font-family: "Khand", sans-serif; font-weight: 600; font-size: 23px; line-height: 1; color: #222; margin-bottom: 10px; }
  .details__line { display: flex; align-items: center; gap: 10px; font-size: 13px; line-height: 17px; }
  .details__line svg { width: 10px; height: 10px; fill: var(--rust); flex: none; }
  .details__address { margin-top: 6px; font-size: 13px; line-height: 17px; }

  .front__band { position: absolute; left: 0; top: 271px; width: 250px; height: 21px; background: var(--rust-dark); }
  .front__bar { position: absolute; left: 0; top: 253px; width: 484px; height: 39px; }
  .front__web { position: absolute; left: 274px; top: 264px; font-family: "Questrial", sans-serif; font-size: 13px; color: var(--web); }
  .front__web b { font-weight: normal; color: var(--rust); }
</style>
</head>
<body>
<div class="canvas">

  <section class="card card--back">
    <div class="wordmark">
      <span class="wordmark__dot"></span>
      <span class="wordmark__name">morlenbay</span>
    </div>
  </section>

  <section class="card card--front">
    <div class="wordmark">
      <span class="wordmark__dot"></span>
      <span class="wordmark__name">morlenbay</span>
    </div>

    <div class="front__divider"></div>

    <div class="details">
      <div class="details__name">Dale Vornhuser</div>
      <div class="details__line">
        <svg viewBox="0 0 10 10"><rect x="2" y="0" width="6" height="10" rx="1"/></svg>240.815.3926
      </div>
      <div class="details__line">
        <svg viewBox="0 0 10 10"><path d="M0 4 Q5 0 10 4 L8 5 L7 3.5 L3 3.5 L2 5 Z M2 6 H8 V10 H2 Z"/></svg>703.461.8075
      </div>
      <div class="details__line">
        <svg viewBox="0 0 10 10"><path d="M0 2 H10 V8 H0 Z M0 2 L5 6 L10 2" stroke="#f4f4f4" stroke-width="0.8"/></svg>dale@morlenbay.com
      </div>
      <div class="details__address">31800 Pinecrest Lane #412<br>Damascus, MD 20879</div>
    </div>

    <div class="front__band"></div>
    <svg class="front__bar" viewBox="0 0 484 39" preserveAspectRatio="none" aria-hidden="true">
      <polygon points="242,39 258,0 484,0 484,39" fill="var(--ink)"/>
    </svg>
    <div class="front__web">www.<b>morlenbay</b>.com</div>
  </section>

</div>
</body>
</html>
```